Postcard: Live Ever Kinder

Text for front: HOW TO CHANGE THE WORLD IN ONE [note: the word "one" should be underlined] STEPHint: It's up to you...[Note: add arrow or something to indicate "turn over"]Text for back: You're going to spend your entire life with someone you can never get away from. (Guess who?) Wouldn't you rather that person #LiveEverKinder than judgmental or critical? BE the change you want to see! Visit www.LiveEverKinder-hub.com for daily Bright Pebbles and community. PLEASE JOIN US![Note: add logo to left half of back side]Font preference for text: Josefin sans

Target Market(s)

People who would be attracted to Calvera church - unitarian universalist message. It's spiritual without being overtly religious, so the target market is probably early 30s and up but ideally won't turn off Millennials (folks under 30). It should attract attention of people who are open-minded and committed to progressive social change, tired of an atmosphere of hate-mongering and divisiveness.

Requirements
Nice to have
• It would be nice to convey a sense of challenge - there is an idea of "bright pebbles" so something related to fire/sparks is appropriate. This is meant to evoke a deeper, divine love more than a sense of romantic love. This love is more fierce than fluffy! Yet it calls us to be our best selves.
Should not have
• Please avoid excessive pink - just the logo is enough, as this design needs to appeal to men as well as women.

```html
<!DOCTYPE html>
<html lang="en">
<head>
<meta charset="utf-8">
<title>Live Ever Kinder – Postcard</title>
<link href="https://fonts.googleapis.com/css2?family=Josefin+Sans:wght@300;400;600&family=Marck+Script&display=swap" rel="stylesheet">
<style>
  :root {
    --page-bg: #ecebe8;
    --front-bg: #c8456b;
    --front-ink: #ffffff;
    --back-bg: #f8f0ea;
    --back-glow: #fdf8f4;
    --back-warm: #f1e3dc;
    --back-ink: #c23c69;
  }
  * { margin: 0; padding: 0; box-sizing: border-box; }
  html, body {
    width: 925px;
    height: 1200px;
    overflow: hidden;
    background: var(--page-bg);
  }
  body { position: relative; font-family: "Josefin Sans", sans-serif; }

  .card {
    position: absolute;
    height: 453px;
    box-shadow: 0 3px 8px rgba(0, 0, 0, 0.18);
  }

  /* Front side */
  .card--front {
    left: 86px;
    top: 93px;
    width: 666px;
    background: var(--front-bg);
    color: var(--front-ink);
  }
  .front__title {
    position: absolute;
    left: 0;
    top: 58px;
    width: 100%;
    text-align: center;
    font-weight: 300;
    font-size: 67px;
    line-height: 81px;
    letter-spacing: 0.5px;
  }
  .front__hint {
    position: absolute;
    left: 50px;
    top: 330px;
    font-family: "Marck Script", cursive;
    font-size: 50px;
    line-height: 1;
  }
  .front__turn-arrow {
    position: absolute;
    left: 480px;
    top: 306px;
    width: 140px;
    height: 115px;
  }

  /* Back side */
  .card--back {
    left: 162px;
    top: 663px;
    width: 670px;
    background: var(--back-bg);
    color: var(--back-ink);
    overflow: hidden;
  }
  .back__glow {
    position: absolute;
    inset: 0;
    background:
      radial-gradient(ellipse at 30% 75%, var(--back-glow) 0%, rgba(253, 248, 244, 0) 60%),
      linear-gradient(180deg, var(--back-warm) 0%, var(--back-bg) 45%, var(--back-glow) 100%);
  }
  .back__brand {
    position: absolute;
    left: 30px;
    top: 100px;
    width: 280px;
    text-align: center;
    font-weight: 400;
    font-size: 34px;
    line-height: 42px;
    letter-spacing: 2px;
    text-transform: uppercase;
  }
  .back__brand-dot {
    display: block;
    width: 14px;
    height: 14px;
    margin: 0 auto 14px;
    border-radius: 50%;
    background: var(--back-ink);
  }
  .back__message {
    position: absolute;
    left: 340px;
    top: 52px;
    width: 320px;
    text-align: center;
    font-weight: 300;
    font-size: 15.5px;
    line-height: 24px;
  }
  .back__message p + p { margin-top: 6px; }
  .back__message strong { font-weight: 600; }
  .back__cta {
    position: absolute;
    left: 0;
    top: 348px;
    width: 100%;
    text-align: center;
    font-weight: 400;
    font-size: 78px;
    line-height: 1;
  }
</style>
</head>
<body>

  <section class="card card--front" aria-label="Postcard front">
    <h1 class="front__title">HOW TO CHANGE<br>THE WORLD<br>IN ONE STEP</h1>
    <p class="front__hint">Hint: It’s up to you...</p>
    <svg class="front__turn-arrow" viewBox="0 0 140 115" aria-label="Turn over" role="img">
      <g fill="none" stroke="#ffffff" stroke-width="4" stroke-linecap="round" stroke-linejoin="round">
        <path d="M58 42 C74 38 80 14 60 8 C32 0 8 28 10 58 C12 92 60 108 132 96"/>
        <path d="M114 80 L133 96 L116 111"/>
      </g>
    </svg>
  </section>

  <section class="card card--back" aria-label="Postcard back">
    <div class="back__glow" role="img" aria-label="Soft warm sparkle background in cream and blush tones"></div>

    <div class="back__brand">
      <span class="back__brand-dot"></span>
      Live<br>Ever<br>Kinder
    </div>

    <div class="back__message">
      <p>You’re going to spend your entire life with someone you can never get away from.</p>
      <p><strong>(Guess who?)</strong></p>
      <p>Wouldn’t you rather that person<br><strong>#LiveEverKinder</strong> than<br>judgmental or critical?<br>BE the change you want to see!</p>
      <p>Visit <strong>www.LiveEverKinder-hub.com</strong><br>for daily Bright Pebbles and community.</p>
    </div>

    <p class="back__cta">PLEASE JOIN US!</p>
  </section>

</body>
</html>
```